Website Redesign for Non-Profit Ministry & Church

NOTE: Please do not contact me privately — all private inquiries will be ignored.

Individuals seeking spiritual healing, community connection, ministry support and journal-based encounters.

Description of What’s Needed

We need a clean, fresh, inviting website that encourages engagement and connection. The site should feel warm and accessible, draw people in, and clearly present who we are, what we offer, and how visitors can participate. The layout should be straightforward, with well-structured pages (no overlapping objects, minimal layering complexity) and easy to navigate. Use only Google Fonts. All stock photos must be sourced from royalty-free sites and include proper attribution. We will not include a search feature.

Pages to Create
1. Home Page – impactful hero area, clear call-to-action, visual story of ministry, giving/gathering invitation.
2. About Us – vision, mission, leadership, testimonies, history.
3. Meetings & Events – upcoming gatherings, schedule, how to attend, sign-up or interest form.
4. Encounter: “Lanterns Over Marrowdale” (book) – dedicated page for the book, overview, purchase link or details, journal prompts, imagery.
5. Quietwater Chambers / Ministry – explain ministry offerings, invite participation, testimonials or case-studies.
6. Live Stream & Links Page – page listing links for StreamVale live stream, other platforms, archive links; simple layout.

Colour & Branding

Use colours that blend with our existing logo (attached). The palette should feel contemporary, welcoming, and aligned with ministry themes of restoration, healing and love. Ensure text, button and link colours maintain good contrast for accessibility.

Existing Content & Reference

Please gather available content from our current website in the attachment here for text, images and structure for reuse.

Imagery Guidelines

– Use original photos from our Gatherbook page or Google Location listing for building or people images when available.
– If generic images are used, ensure they depict appropriate ministry-related buildings or people (community, warm gathering) — avoid generic unrelated stock imagery.
– All photos must be royalty-free or have proper licensing and attribution.
– No overlapping objects or visual clutter; clean layouts with defined sections.

Additional Notes

– Integration: We currently utilise MailChimp for email communication; the design should include a connection/invite to subscribe (via MailChimp) but no blog page is required at this time.
– Payment/Giving: We accept PayPal and already have a giving portal; include clear donation/give buttons or calls-to-action linking to existing giving systems.
– No search function to be included.
– Layouts should avoid complex layering or overlapping elements—designers should work with distinct content blocks, clear visual hierarchy, and straightforward mobile-friendly structure.

Target Market(s)

Industry/Entity Type

Church/Religious institution

Number of Pages Required

5+ page

Requirements
Should not have
• search bar

```html
<!DOCTYPE html>
<html lang="en">
<head>
<meta charset="utf-8">
<title>Mended Held Whole — Website Pages</title>
<link rel="stylesheet" href="https://fonts.googleapis.com/css2?family=Lexend:wght@300;400;500;600&display=swap">
<style>
:root{
  --green:#17927a;--green-d:#0f7a64;--purple:#6b2d9e;--purple-d:#56218a;
  --teal-l:#9adfd2;--ink:#4a4a55;--muted:#7a7a84;--line:#e4e0ea;--soft:#f6f3fa;
}
*{box-sizing:border-box}
html,body{margin:0;width:1200px;height:2503px;overflow:hidden;background:#fff}
body{position:relative;font-family:'Lexend',sans-serif;color:var(--ink)}
p{margin:0}
.board-logo{position:absolute;left:522px;top:42px;display:flex;align-items:center;gap:9px}
.board-logo .mark{width:46px;height:46px;border-radius:50%;background:var(--green)}
.board-logo .name{color:var(--green);font-weight:600;font-size:19px;line-height:20px}
.board-title{position:absolute;width:352px;text-align:center;font-weight:600;font-size:25px;letter-spacing:-.3px;white-space:nowrap;line-height:30px}
.board-title.long{font-size:21px;letter-spacing:-.4px}
.t-green{color:var(--green-d)}.t-purple{color:var(--purple)}
.page{position:absolute;width:352px;background:#fff;box-shadow:0 0 0 1px #ececf0,0 3px 8px rgba(40,20,70,.06);overflow:hidden;font-size:3.7px;line-height:1.8;font-weight:300}
.site-head{height:37px;display:flex;flex-direction:column;align-items:center;justify-content:space-between;padding-top:6px}
.site-logo{display:flex;align-items:center;gap:3px}
.site-logo i{width:11px;height:11px;border-radius:50%;background:var(--green);display:block}
.site-logo span{color:var(--green);font-weight:600;font-size:4.4px;line-height:4.6px}
.nav{display:flex;gap:9px;font-size:3.2px;text-transform:uppercase;color:#555;padding-bottom:2px;font-weight:400}
.nav .on{color:var(--purple)}
.hero{position:relative;height:115px}
.hero .photo{position:absolute;inset:0}
.hero-card{position:absolute;right:14px;bottom:14px;width:98px;height:62px;background:#fff;border-radius:10px;box-shadow:3px 3px 0 var(--teal-l);display:flex;flex-direction:column;align-items:center;justify-content:center;text-align:center;color:var(--green-d);font-weight:500;font-size:7.5px;line-height:1.4;text-transform:uppercase}
.hero-card .dot{width:7px;height:7px;border:1px solid var(--green);border-radius:50%;margin-bottom:4px}
.sec-head{display:flex;align-items:center;justify-content:center;gap:4px;font-size:7px;font-weight:500;color:var(--green-d);text-transform:uppercase;line-height:1.3}
.sec-head b{font-weight:500;color:var(--purple)}
.sec-head::before{content:"";flex:none;width:6px;height:6px;border:1px solid var(--green);border-radius:50%}
.sec-head.left{justify-content:flex-start}
.purple{background:linear-gradient(135deg,var(--purple),var(--purple-d));color:#fff}
.purple .sec-head{color:#fff}.purple .sec-head b{color:var(--teal-l)}.purple .sec-head::before{border-color:var(--teal-l)}
.btn{display:inline-block;background:var(--green);color:#fff;font-size:3.3px;font-weight:500;padding:2px 8px;border-radius:2px;text-transform:uppercase;line-height:1.8}
.btn.ghost{background:#fff;color:var(--green);border:.6px solid var(--green)}
.center{text-align:center}
.lead{width:290px;margin:8px auto 0;text-align:center;color:var(--muted)}
.accent{color:var(--green)}
.sub{font-size:4.4px;color:var(--green-d);font-weight:500;text-transform:uppercase;margin:6px 0 2px}
.sub.purple-t{color:var(--purple)}
.frame{border-radius:18px;box-shadow:4px 4px 0 var(--teal-l)}
.abs{position:absolute}
.rel{position:relative}
.site-foot{position:relative;background:linear-gradient(135deg,var(--purple),var(--purple-d));color:#fff}
.foot-brand{position:absolute;left:30px;top:24px}
.foot-brand .lg{display:flex;align-items:center;gap:4px}
.foot-brand .lg i{width:20px;height:20px;border-radius:50%;background:var(--teal-l);display:block}
.foot-brand .lg span{font-weight:600;font-size:8px;line-height:8px}
.social{display:flex;gap:4px;margin:6px 0 0 22px}
.social i{width:8px;height:8px;border:.6px solid #fff;border-radius:50%;display:block}
.foot-col{position:absolute;top:22px;font-size:3.1px;line-height:2.1;text-transform:uppercase;font-weight:400}
.foot-col h6{margin:0 0 1px;font-size:3.5px;font-weight:400;color:var(--teal-l)}
.copy{position:absolute;left:0;right:0;bottom:9px;text-align:center;font-size:3.1px;text-transform:uppercase}
.quotes{display:grid;grid-template-columns:110px 110px;gap:10px 40px;justify-content:center;margin-top:14px}
.quote{position:relative;height:76px;border:.6px solid var(--line);border-radius:8px;padding:8px 10px;font-size:3.3px;color:var(--muted);line-height:2}
.quote .who{color:var(--green);margin-top:3px;text-transform:uppercase}
.quote .qm{position:absolute;right:8px;bottom:2px;font-size:14px;color:#e3e3e8;font-weight:600;line-height:1}
.events{display:grid;grid-template-columns:repeat(3,88px);gap:12px 10px;justify-content:center;margin-top:10px}
.event .ph{height:62px;border-radius:6px}
.event .meta{font-size:3.1px;line-height:2;margin-top:5px;text-transform:uppercase}
.event .meta span::before{content:"";display:inline-block;width:3px;height:3px;background:var(--purple);border-radius:1px;margin-right:3px;vertical-align:middle}
.event h4{margin:3px 0 1px;font-size:3.5px;color:var(--green-d);font-weight:500;text-transform:uppercase}
.event p{font-size:3.2px;color:var(--muted);line-height:2;height:26px}
.event .btn{font-size:3px;padding:1px 6px}
.field{position:absolute;height:13px;border:.6px solid #d9d6df;border-radius:2px;font-size:3px;color:#999;padding:3px 5px;text-transform:uppercase}
.card-s{position:absolute;border:.6px solid var(--line);border-radius:8px;background:#fff}
.prompt{border-bottom:.6px solid var(--line);padding:5px 0;font-size:3.6px;text-transform:uppercase;color:#555;font-weight:400}
.icon-box{width:16px;height:16px;border:.8px solid currentColor;border-radius:4px;display:block}
</style>
</head>
<body>

<div class="board-logo"><span class="mark"></span><span class="name">Mended<br>Held<br>Whole</span></div>

<div class="board-title t-green" style="left:39px;top:160px">HOME PAGE</div>
<div class="board-title t-purple" style="left:424px;top:160px">ABOUT US</div>
<div class="board-title t-green" style="left:810px;top:160px">MEETINGS &amp; EVENTS</div>
<div class="board-title t-green" style="left:39px;top:1457px">ENCOUNTER</div>
<div class="board-title long t-purple" style="left:400px;top:1459px;width:400px">QUIETWATER CHAMBERS / MINISTRY</div>
<div class="board-title t-green" style="left:810px;top:1457px">LIVE STREAM</div>

<!-- ================= HOME ================= -->
<section class="page" style="left:39px;top:200px;height:899px">
  <header class="site-head">
    <div class="site-logo"><i></i><span>Mended<br>Held<br>Whole</span></div>
    <nav class="nav"><span class="on">Home</span><span>About Us</span><span>Meetings &amp; Events</span><span>Encounter</span><span>Quietwater Chambers / Ministry</span><span>Live Stream &amp; Links</span></nav>
  </header>
  <div class="hero" style="height:150px">
    <div class="photo" role="img" aria-label="Congregation seated in a bright chapel listening to a speaker" style="background:linear-gradient(180deg,#d8cbb6 0%,#b69a78 45%,#5d4a7a 80%,#3d3466 100%)"></div>
    <div class="hero-card" style="bottom:22px;height:66px"><span class="dot"></span>Mended, Held,<br>Whole</div>
  </div>
  <div class="rel" style="height:200px">
    <div class="abs frame" role="img" aria-label="Brick church building at dusk" style="left:34px;top:22px;width:108px;height:150px;background:linear-gradient(170deg,#8fb6d8 0%,#9a5a44 55%,#3b2c2a 100%)"></div>
    <div class="abs" style="left:170px;top:28px;width:152px;color:var(--muted)">
      <div class="sec-head left">Our Mission <b>&amp; Vision</b></div>
      <p style="margin-top:6px">Honoring God's presence by loving the broken, seeking the lost, and healing the hurting through the demonstration of His love and power. Mended, Held, Whole is here to activate, proclaim and teach the love of the Father through Jesus with the guidance of the Holy Spirit.</p>
      <div class="sub">Story of Ministry</div>
      <p>Our ministry exists to help people encounter God through worship, prayer, and authentic connection. We believe in healing, compassion, discipleship, and the transformative love of Jesus.</p>
      <div style="margin-top:8px"><span class="btn">Learn More</span> <span class="btn ghost" style="margin-left:4px">Invite</span></div>
    </div>
  </div>
  <div class="purple rel" style="height:168px">
    <div class="abs" style="left:30px;top:22px;width:160px">
      <div class="sec-head left">Encounter: <b>Lanterns Over</b></div>
      <div style="font-size:7px;color:var(--teal-l);margin-left:10px;line-height:1.3">MARROWDALE</div>
      <p style="margin-top:7px">Encounter: Lanterns Over Marrowdale begins with the astounding story of Ada's journey through difficult times, including many years of suffering through Bipolar Disorder to a healing encounter with Jesus.</p>
      <p style="margin-top:4px">The book is a six-week guided journal with a short daily devotion. The first week examines the "I am" statements of Jesus found in the Gospel of John.</p>
      <div style="margin-top:8px"><span class="btn">Book Now</span></div>
    </div>
    <div class="abs" role="img" aria-label="Book cover with lanterns and yellow flowers in a dark green wood" style="left:205px;top:18px;width:102px;height:134px;border-radius:16px;background:linear-gradient(170deg,#1f3b2e,#2e5a3a 55%,#8a8a2a 80%,#17261f)"></div>
  </div>
  <div style="height:145px;padding-top:24px" class="center">
    <div class="sec-head">Who <b>We Are</b></div>
    <p class="lead">Tobias and Ada have been married for 42 years and have two adult children. They both grew up in the southern hills. Their desire is to share the love of Christ with others. They have numerous stories to share about the many ways they have seen God move in their lives as well as the lives of others. They believe in the manifestation of God's power through signs and wonders. They have not only witnessed God's power through signs and wonders them they have also experienced His miraculous healing touch personally.</p>
    <div style="margin-top:8px"><span class="btn">Learn More</span></div>
  </div>
  <div class="rel" style="height:90px;background:linear-gradient(#fff 0 42px,var(--purple) 42px)">
    <div class="abs center" style="left:42px;top:6px;width:268px;height:76px;background:#fff;border:.6px solid var(--line);border-radius:6px;padding-top:10px">
      <div class="sec-head">Join Our <b>Newsletter</b></div>
      <p style="color:var(--muted);margin-top:4px">Signup today for free and be the first to get notified on new updates.</p>
      <div class="field" style="left:18px;top:46px;width:66px">Enter your email</div>
      <div class="field" style="left:90px;top:46px;width:66px">Enter first name</div>
      <div class="field" style="left:162px;top:46px;width:66px">Enter last name</div>
      <span class="btn abs" style="left:234px;top:47px;padding:2px 5px">Subscribe</span>
    </div>
  </div>
  <footer class="site-foot" style="height:109px">
    <div class="foot-brand"><div class="lg"><i></i><span>Mended<br>Held<br>Whole</span></div><div class="social"><i></i><i></i></div></div>
    <div class="foot-col" style="left:135px"><h6>Quick Links</h6>Home<br>About Us<br>Meetings &amp; Events<br>Encounter<br>Quietwater Chambers / Ministry<br>Live Stream &amp; Links</div>
    <div class="foot-col" style="left:232px"><h6>Recent Posts</h6>Nothing is incurable for God<br>Healing amidst the car accident<br>Healing – where and how can it happen?<br>Why is healing important?<br>Now is the time to move</div>
    <div class="copy">Copyright © 2026. All rights reserved.</div>
  </footer>
</section>

<!-- ================= ABOUT ================= -->
<section class="page" style="left:424px;top:200px;height:1100px">
  <header class="site-head">
    <div class="site-logo"><i></i><span>Mended<br>Held<br>Whole</span></div>
    <nav class="nav"><span>Home</span><span class="on">About Us</span><span>Meetings &amp; Events</span><span>Encounter</span><span>Quietwater Chambers / Ministry</span><span>Live Stream &amp; Links</span></nav>
  </header>
  <div class="hero">
    <div class="photo" role="img" aria-label="Sunlit church sanctuary with wooden pews and an altar cross" style="background:linear-gradient(180deg,#c9b9a2 0%,#7b5f44 50%,#2e2420 100%)"></div>
    <div class="hero-card" style="height:56px"><span class="dot"></span>About Us</div>
  </div>
  <div class="center" style="height:116px;padding-top:22px">
    <div class="sec-head">Mended Held Whole <b>Vision</b></div>
    <p class="lead" style="width:290px">We are a Christ-centered ministry and church community committed to creating a welcoming space where people can encounter God, experience healing, and grow in peace and wholeness. Our heart is to walk alongside individuals and families from all backgrounds, offering a place of restoration, prayer, learning, and genuine connection. Whether you are exploring faith for the first time or have walked with God for many years, you are welcome here. <span class="accent">To see lives restored, hearts mended, and communities transformed through the love and presence of God.</span></p>
  </div>
  <div class="purple rel" style="height:163px;padding-top:22px">
    <div class="sec-head">Mended Held Whole <b>Mission</b></div>
    <div style="display:flex;gap:8px;justify-content:center;margin-top:14px">
      <div style="width:62px;height:100px;background:rgba(255,255,255,.13);border-radius:8px;text-align:center;padding:14px 5px 0"><span class="icon-box" style="margin:0 auto 10px;color:#fff;border-radius:50%"></span>To create safe, compassionate spaces for spiritual healing and growth</div>
      <div style="width:62px;height:100px;background:rgba(255,255,255,.13);border-radius:8px;text-align:center;padding:14px 5px 0"><span class="icon-box" style="margin:0 auto 10px;color:#fff"></span>To encourage deeper relationship with God through prayer, teaching, and reflection</div>
      <div style="width:62px;height:100px;background:rgba(255,255,255,.13);border-radius:8px;text-align:center;padding:14px 5px 0"><span class="icon-box" style="margin:0 auto 10px;color:#fff;border-radius:50%"></span>To support individuals on their personal journey toward peace and wholeness</div>
      <div style="width:62px;height:100px;background:rgba(255,255,255,.13);border-radius:8px;text-align:center;padding:14px 5px 0"><span class="icon-box" style="margin:0 auto 10px;color:#fff"></span>To serve our community with humility, love, and integrity</div>
    </div>
  </div>
  <div style="height:306px;padding-top:22px">
    <div class="sec-head">Our <b>Testimonials</b></div>
    <div class="quotes">
      <div class="quote">"I walked in feeling overwhelmed and unsure, but I was met with kindness and understanding. This ministry became a place where I could slow down, pray, and find peace again."<div class="who">– Hannah P</div><span class="qm">”</span></div>
      <div class="quote">"During a difficult season in my life, the prayer and support I received here brought comfort and healing. I felt heard, supported, and deeply cared for."<div class="who">– Owen B</div><span class="qm">”</span></div>
      <div class="quote">"From the very first visit, I felt welcomed. There was no pressure—just genuine love and a sense of belonging. This community has truly become home for me."<div class="who">– Lucia F</div><span class="qm">”</span></div>
      <div class="quote">"I came searching for answers and found hope. Through worship, teaching, and prayer, I experienced restoration in my heart and clarity in my life."<div class="who">– Anonymous</div><span class="qm">”</span></div>
      <div class="quote">"This ministry doesn't just offer services—it walks with you. The encouragement and guidance I received helped me reconnect with my faith and move forward with confidence."<div class="who">– Peter G</div><span class="qm">”</span></div>
      <div class="quote">"The environment here is calm, prayerful, and deeply caring. I leave each gathering feeling renewed, grounded, and reminded that I'm not alone."<div class="who">– Naomi S</div><span class="qm">”</span></div>
    </div>
  </div>
  <div class="rel" style="height:250px">
    <div class="abs frame" role="img" aria-label="Ministry founders, a smiling couple, before a stained glass window" style="left:34px;top:6px;width:112px;height:122px;background:linear-gradient(150deg,#4a6fb0,#b0453c 45%,#2a2a3a 100%)"></div>
    <div class="abs" style="left:170px;top:6px;width:152px;color:var(--muted)">
      <div class="sec-head left">Our <b>History</b></div>
      <p style="margin-top:5px">Our journey began with a simple desire: to create space for people to encounter God in a personal and meaningful way.</p>
      <p style="margin-top:3px">What started as small prayer gatherings and intimate times of reflection gradually grew into a ministry rooted in healing, restoration, and compassionate community. From the beginning, the focus has never been on size or visibility, but on faithfulness: listening to God, caring for people, and responding to real needs.</p>
      <p style="margin-top:3px">As the ministry continued to grow, gatherings expanded, and new expressions of service emerged, including healing prayer, teaching, and guided spiritual practices designed to support people in their everyday lives. Each step forward has been shaped by prayer, discernment, and a commitment to serve with humility and love.</p>
    </div>
    <div class="abs" style="left:34px;top:166px;width:288px;color:var(--muted)">
      <p>Over the years, countless individuals and families have walked through our doors seeking peace, clarity, or healing. Many have found not only spiritual renewal, but also a supportive community willing to walk alongside them through life's challenges.</p>
      <p style="margin-top:4px">Today, we remain committed to the same foundation on which we were built—creating a safe, welcoming environment where people can grow in faith, experience restoration, and encounter God's presence in a real and lasting way. As we look ahead, we continue to trust God's leading, believing that the best work is still unfolding, one life at a time.</p>
    </div>
  </div>
  <footer class="site-foot" style="height:115px">
    <div class="foot-brand"><div class="lg"><i></i><span>Mended<br>Held<br>Whole</span></div><div class="social"><i></i><i></i></div></div>
    <div class="foot-col" style="left:135px"><h6>Quick Links</h6>Home<br>About Us<br>Meetings &amp; Events<br>Encounter<br>Quietwater Chambers / Ministry<br>Live Stream &amp; Links</div>
    <div class="foot-col" style="left:232px"><h6>Recent Posts</h6>Nothing is incurable for God<br>Healing amidst the car accident<br>Healing – where and how can it happen?<br>Why is healing important?<br>Now is the time to move</div>
    <div class="copy">Copyright © 2026. All rights reserved.</div>
  </footer>
</section>

<!-- ================= MEETINGS ================= -->
<section class="page" style="left:810px;top:200px;height:1209px">
  <header class="site-head">
    <div class="site-logo"><i></i><span>Mended<br>Held<br>Whole</span></div>
    <nav class="nav"><span>Home</span><span>About Us</span><span class="on">Meetings &amp; Events</span><span>Encounter</span><span>Quietwater Chambers / Ministry</span><span>Live Stream &amp; Links</span></nav>
  </header>
  <div class="hero">
    <div class="photo" role="img" aria-label="Speaker and guitarist leading a warm evening gathering" style="background:linear-gradient(160deg,#2a1f1a 0%,#7a5234 45%,#c49060 70%,#3a2a22 100%)"></div>
    <div class="hero-card" style="height:64px"><span class="dot"></span>Meetings &amp;<br>Events</div>
  </div>
  <div style="height:487px;padding-top:22px" class="center">
    <div class="sec-head">Join Us For Our <b>Gatherings</b></div>
    <p class="lead">We invite you to join us for our regular meetings and special events. Each gathering is an opportunity to connect, reflect, worship, and experience God's presence in a peaceful and welcoming environment.</p>
    <p class="lead" style="margin-top:2px">Whether you are attending for the first time or returning regularly, you are warmly welcome.</p>
    <div class="sec-head" style="margin-top:16px">Upcoming <b>Gatherings</b></div>
    <div class="events" style="text-align:left">
      <div class="event"><div class="ph" role="img" aria-label="Worship hall facing a lit cross" style="background:linear-gradient(170deg,#5a2a22,#b46a42 60%,#2a1a16)"></div><div class="meta"><span>Sunday, March 15</span><br><span>10:00 AM – 11:30 AM</span></div><h4>Sunday Worship Gathering</h4><p>A welcoming time of worship, prayer, and teaching focused on renewal, peace, and community.</p><span class="btn">Join Us</span></div>
      <div class="event"><div class="ph" role="img" aria-label="Candlelit evening prayer" style="background:linear-gradient(170deg,#2a1a12,#a8682e 60%,#1e140e)"></div><div class="meta"><span>Wednesday, March 18</span><br><span>7:00 PM – 8:00 PM</span></div><h4>Midweek Prayer &amp; Reflection</h4><p>A quiet, guided time of prayer and reflection designed to help you slow down and reconnect with God.</p><span class="btn">Attend Prayer Night</span></div>
      <div class="event"><div class="ph" role="img" aria-label="Chapel with glowing cross" style="background:linear-gradient(170deg,#7a3a22,#e0a060 55%,#5a2a1a)"></div><div class="meta"><span>Friday, March 21</span><br><span>6:00 PM – 8:30 PM</span></div><h4>Quietwater Chambers Ministry</h4><p>One-on-one prayer and ministry sessions offering support, encouragement, and spiritual care.</p><span class="btn">Request a Session</span></div>
      <div class="event"><div class="ph" role="img" aria-label="Evening gathering under a dusk sky" style="background:linear-gradient(170deg,#2a3a6a,#6a4a6a 55%,#1a1622)"></div><div class="meta"><span>Saturday, March 29</span><br><span>5:30 PM – 8:00 PM</span></div><h4>Encounter Evening</h4><p>An extended evening of worship, teaching, &amp; guided reflection centered on healing &amp; personal encounter.</p><span class="btn">Register Interest</span></div>
      <div class="event"><div class="ph" role="img" aria-label="Fellowship hall with shared tables" style="background:linear-gradient(170deg,#6a3a1e,#c08040 55%,#3a2212)"></div><div class="meta"><span>Sunday, April 6</span><br><span>9:00 AM – 9:45 AM</span></div><h4>Community Fellowship Morning</h4><p>An informal gathering with conversation, refreshments, and connection before the worship service.</p><span class="btn">Join Fellowship</span></div>
      <div class="event"><div class="ph" role="img" aria-label="Congregation listening to a speaker" style="background:linear-gradient(170deg,#4a3a30,#8a6a50 55%,#2a221e)"></div><div class="meta"><span>Tuesday, April 8</span><br><span>7:00 PM – 8:00 PM</span></div><h4>Online Prayer Gathering</h4><p>A virtual prayer gathering for those unable to attend in person.</p><span class="btn">Join Online</span></div>
    </div>
  </div>
  <div class="purple center" style="height:102px;padding-top:22px">
    <div class="sec-head">New To Our <b>Community?</b></div>
    <p style="width:280px;margin:7px auto 0">If you're attending for the first time, we'd love to help you feel comfortable. Our team is available to answer questions, provide directions, or assist you with next steps.</p>
    <div style="margin-top:7px"><span class="btn">Schedule Now</span></div>
  </div>
  <div class="rel" style="height:155px;padding-top:24px">
    <div class="sec-head">How To <b>Attend</b></div>
    <div class="card-s" style="left:42px;top:46px;width:78px;height:95px;padding:8px;color:var(--muted)"><span class="abs" style="right:6px;top:6px;width:10px;height:10px;border-radius:50%;background:var(--green-d);color:#fff;font-size:3.2px;text-align:center;line-height:10px">01</span><span class="icon-box" style="color:var(--purple);margin:10px 0 8px"></span><div style="color:var(--green-d);text-transform:uppercase;font-weight:400">Choose a Gathering</div>Review the upcoming meetings and select the one that fits your schedule.</div>
    <div class="card-s" style="left:137px;top:46px;width:78px;height:95px;padding:8px;color:var(--muted)"><span class="abs" style="right:6px;top:6px;width:10px;height:10px;border-radius:50%;background:var(--purple);color:#fff;font-size:3.2px;text-align:center;line-height:10px">02</span><span class="icon-box" style="color:var(--purple);margin:10px 0 8px"></span><div style="color:var(--green-d);text-transform:uppercase;font-weight:400">Attend in Person or Online</div>Join us at our physical location or connect through our live stream when available.</div>
    <div class="card-s" style="left:232px;top:46px;width:78px;height:95px;padding:8px;color:var(--muted)"><span class="abs" style="right:6px;top:6px;width:10px;height:10px;border-radius:50%;background:var(--green-d);color:#fff;font-size:3.2px;text-align:center;line-height:10px">03</span><span class="icon-box" style="color:var(--purple);margin:10px 0 8px;border-radius:50%"></span><div style="color:var(--green-d);text-transform:uppercase;font-weight:400">Come As You Are</div>There is no dress code or expectation—just come as you are and take part at your own pace.</div>
  </div>
  <div class="rel center" style="height:199px;padding-top:14px">
    <div class="sec-head">Sign Up / <b>Express Interest</b></div>
    <p class="lead" style="width:270px;margin-top:5px">Use the form below to let us know you're planning to attend, request more information, or receive updates about upcoming gatherings and events.</p>
    <div class="field" style="left:50px;top:52px;width:120px;text-align:left">Full Name</div>
    <div class="field" style="left:180px;top:52px;width:120px;text-align:left">Email Address</div>
    <div class="field" style="left:50px;top:76px;width:120px;text-align:left">Phone Number</div>
    <div class="field" style="left:180px;top:76px;width:120px;text-align:left">Gathering of Interest<span style="float:right">▾</span></div>
    <div class="field" style="left:50px;top:100px;width:250px;height:32px;text-align:left">Message or Questions</div>
    <span class="btn abs" style="left:155px;top:146px">Submit Now</span>
  </div>
  <footer class="site-foot" style="height:114px">
    <div class="foot-brand"><div class="lg"><i></i><span>Mended<br>Held<br>Whole</span></div><div class="social"><i></i><i></i></div></div>
    <div class="foot-col" style="left:135px"><h6>Quick Links</h6>Home<br>About Us<br>Meetings &amp; Events<br>Encounter<br>Quietwater Chambers / Ministry<br>Live Stream &amp; Links</div>
    <div class="foot-col" style="left:232px"><h6>Recent Posts</h6>Nothing is incurable for God<br>Healing amidst the car accident<br>Healing – where and how can it happen?<br>Why is healing important?<br>Now is the time to move</div>
    <div class="copy">Copyright © 2026. All rights reserved.</div>
  </footer>
</section>

<!-- ================= ENCOUNTER ================= -->
<section class="page" style="left:39px;top:1497px;height:868px">
  <header class="site-head">
    <div class="site-logo"><i></i><span>Mended<br>Held<br>Whole</span></div>
    <nav class="nav"><span>Home</span><span>About Us</span><span>Meetings &amp; Events</span><span class="on">Encounter</span><span>Quietwater Chambers / Ministry</span><span>Live Stream &amp; Links</span></nav>
  </header>
  <div class="hero">
    <div class="photo" role="img" aria-label="Open journal and pen on a cosy knitted blanket" style="background:linear-gradient(160deg,#e8ddd0 0%,#c8b49c 50%,#8a7460 100%)"></div>
    <div class="hero-card" style="height:56px"><span class="dot"></span>Encounter</div>
  </div>
  <div class="center" style="height:449px;padding-top:22px">
    <div class="sec-head">Encounter: Lanterns Over Marrowdale –</div>
    <div style="font-size:7px;color:var(--purple);font-weight:500;margin-top:3px">MENDED, HELD, WHOLE</div>
    <div role="img" aria-label="Book cover with lanterns and yellow flowers in a dark green wood" style="width:102px;height:134px;margin:12px auto 0;border-radius:16px;background:linear-gradient(170deg,#1f3b2e,#2e5a3a 55%,#8a8a2a 80%,#17261f)"></div>
    <div style="width:296px;margin:12px auto 0;color:var(--muted)">
      <p><span class="accent">Encounter: Lanterns Over Marrowdale</span> begins with the astounding story of Ada's journey through difficult times, including many years of suffering from Bipolar Disorder to a healing encounter with Jesus.</p>
      <p style="margin-top:4px">The book is a six-week guided journal with a short daily devotion. The first week examines the "I am" statements of Jesus found in the Gospel of John. The following five weeks will focus on Scriptures and identify "I am" statements that will unveil who you are in the eyes of God.</p>
      <p style="margin-top:4px">Each day has "I am" statements, which are affirmations that bring a shift in the mind and emotions of the individual. These are followed by reflective questions, guiding the reader on a journey to peace. What makes this journal unique is the ability to purchase a digital format where you can receive messages by email or text with the daily devotions, affirmations, and questions. You can record your answers in the printed journal or the digital format. The digital daily messages will be reminders to journal and will help with consistency. You can respond to the text messages. If you have questions, each week a live call will be included to supplement the material. You will be added to our prayer list, and we will pray for you daily during your experience.</p>
      <p style="margin-top:4px" class="accent">If you live in the area, you can obtain your copy at Mended, Held, Whole. It is also available on Riverstall.</p>
      <p style="margin-top:4px">The digital format can be obtained here. You are asked to make a suggested minimum donation of $5.00 to cover the cost, along with your name, phone number (text), and email address. Please state in the comments you want the digital version of Encounter: Lanterns Over Marrowdale. Please let us know if you want to select a later start date. If you have any questions, please contact us. If you want to use them together, make sure you have the printed version before beginning the digital version.</p>
      <p style="margin-top:4px">(Click below for the digital version. Make sure you state in the comment section that you want to receive the digital version.)</p>
    </div>
    <div style="margin-top:8px"><span class="btn">Digital Version</span></div>
  </div>
  <div style="height:150px;padding-top:10px">
    <div class="sec-head">Sample Journal <b>Prompts</b></div>
    <div style="width:270px;margin:6px auto 0">
      <div class="prompt">What is weighing on my heart today, and where do I need peace?</div>
      <div class="prompt">What am I being invited to release in this season?</div>
      <div class="prompt">Where have I noticed God's presence, even in small ways?</div>
      <div class="prompt">What does peace look like for me right now?</div>
      <div class="prompt" style="border:0">What am I grateful for today, even in difficulty?</div>
    </div>
  </div>
  <footer class="site-foot" style="height:117px">
    <div class="foot-brand"><div class="lg"><i></i><span>Mended<br>Held<br>Whole</span></div><div class="social"><i></i><i></i></div></div>
    <div class="foot-col" style="left:135px"><h6>Quick Links</h6>Home<br>About Us<br>Meetings &amp; Events<br>Encounter<br>Quietwater Chambers / Ministry<br>Live Stream &amp; Links</div>
    <div class="foot-col" style="left:232px"><h6>Recent Posts</h6>Nothing is incurable for God<br>Healing amidst the car accident<br>Healing – where and how can it happen?<br>Why is healing important?<br>Now is the time to move</div>
    <div class="copy">Copyright © 2026. All rights reserved.</div>
  </footer>
</section>

<!-- ================= QUIETWATER CHAMBERS ================= -->
<section class="page" style="left:424px;top:1497px;height:953px">
  <header class="site-head">
    <div class="site-logo"><i></i><span>Mended<br>Held<br>Whole</span></div>
    <nav class="nav"><span>Home</span><span>About Us</span><span>Meetings &amp; Events</span><span>Encounter</span><span class="on">Quietwater Chambers / Ministry</span><span>Live Stream &amp; Links</span></nav>
  </header>
  <div class="hero">
    <div class="photo" role="img" aria-label="Two people in quiet, hopeful prayer in warm light" style="background:linear-gradient(90deg,#5a3a28 0%,#c49a72 45%,#e8cfa8 70%,#b08a66 100%)"></div>
    <div class="hero-card" style="width:104px;height:64px"><span class="dot"></span>Quietwater<br>Chambers Ministry</div>
  </div>
  <div class="rel" style="height:213px">
    <div class="abs" style="left:0;right:0;top:22px"><div class="sec-head">Quietwater Chambers <b>Ministry</b></div></div>
    <div class="abs" style="left:34px;top:48px;width:80px;color:var(--muted)">
      <p>The Quietwater Chambers Ministry exists to provide a peaceful and supportive environment where individuals can receive prayer, encouragement, and spiritual care.</p>
      <p style="margin-top:5px">Our heart is to walk alongside people during times of need—offering prayer grounded in compassion, respect, and faith.</p>
    </div>
    <div class="abs frame" role="img" aria-label="Person sitting in meditative prayer in a sunlit meadow" style="left:128px;top:50px;width:84px;height:140px;background:linear-gradient(170deg,#e8d6a0,#9aa060 55%,#4a5a2a)"></div>
    <div class="abs" style="left:228px;top:52px;width:92px;color:var(--muted)">
      <div class="sub purple-t" style="font-size:3.6px;margin-top:0">Personal Prayer Sessions</div>
      <p>One-on-one prayer sessions with trained ministry team members who listen with care and pray with you in a confidential and respectful setting.</p>
      <div class="sub purple-t" style="font-size:3.6px">Spiritual Encouragement</div>
      <p>Support for those navigating emotional, spiritual, or life challenges, offered through prayer and gentle guidance.</p>
    </div>
  </div>
  <div class="purple rel" style="height:155px">
    <div class="abs" style="left:0;right:0;top:18px"><div class="sec-head">How To <b>Participate</b></div></div>
    <div class="abs" role="img" aria-label="Hands holding a lit candle in prayer" style="left:34px;top:42px;width:62px;height:88px;border-radius:12px;background:linear-gradient(170deg,#3a2010,#c07a30 55%,#2a160a)"></div>
    <div class="abs" style="left:102px;top:44px;width:66px">
      <div style="color:var(--teal-l);font-size:3.4px;text-transform:uppercase">Receive Prayer</div>
      <p>You may request a Quietwater Chambers session by submitting a request through our sign-up form. Appointments are scheduled based on availability.</p>
      <span class="btn" style="margin-top:5px">Request Prayer</span>
    </div>
    <div class="abs" role="img" aria-label="Illustration of a team gathered around a cross" style="left:188px;top:42px;width:62px;height:88px;border-radius:12px;background:linear-gradient(170deg,#ffffff,#c8d8f0 55%,#5a7ab0)"></div>
    <div class="abs" style="left:256px;top:44px;width:68px">
      <div style="color:var(--teal-l);font-size:3.4px;text-transform:uppercase">Serve With Us</div>
      <p>If you feel called to serve on the Quietwater Chambers Ministry team, we welcome inquiries. Training and support are provided.</p>
      <span class="btn" style="margin-top:5px">Join the Team</span>
    </div>
  </div>
  <div style="height:317px;padding-top:24px">
    <div class="sec-head">Our <b>Testimonials</b></div>
    <div class="quotes">
      <div class="quote">"I walked in feeling overwhelmed and unsure, but I was met with kindness and understanding. This ministry became a place where I could slow down, pray, and find peace again."<div class="who">– Hannah P</div><span class="qm">”</span></div>
      <div class="quote">"During a difficult season in my life, the prayer and support I received here brought comfort and healing. I felt heard, supported, and deeply cared for."<div class="who">– Owen B</div><span class="qm">”</span></div>
      <div class="quote">"From the very first visit, I felt welcomed. There was no pressure—just genuine love and a sense of belonging. This community has truly become home for me."<div class="who">– Lucia F</div><span class="qm">”</span></div>
      <div class="quote">"I came searching for answers and found hope. Through worship, teaching, and prayer, I experienced restoration in my heart and clarity in my life."<div class="who">– Anonymous</div><span class="qm">”</span></div>
      <div class="quote">"This ministry doesn't just offer services—it walks with you. The encouragement and guidance I received helped me reconnect with my faith and move forward with confidence."<div class="who">– Peter G</div><span class="qm">”</span></div>
      <div class="quote">"The environment here is calm, prayerful, and deeply caring. I leave each gathering feeling renewed, grounded, and reminded that I'm not alone."<div class="who">– Naomi S</div><span class="qm">”</span></div>
    </div>
  </div>
  <footer class="site-foot" style="height:116px">
    <div class="foot-brand"><div class="lg"><i></i><span>Mended<br>Held<br>Whole</span></div><div class="social"><i></i><i></i></div></div>
    <div class="foot-col" style="left:135px"><h6>Quick Links</h6>Home<br>About Us<br>Meetings &amp; Events<br>Encounter<br>Quietwater Chambers / Ministry<br>Live Stream &amp; Links</div>
    <div class="foot-col" style="left:232px"><h6>Recent Posts</h6>Nothing is incurable for God<br>Healing amidst the car accident<br>Healing – where and how can it happen?<br>Why is healing important?<br>Now is the time to move</div>
    <div class="copy">Copyright © 2026. All rights reserved.</div>
  </footer>
</section>

<!-- ================= LIVE STREAM ================= -->
<section class="page" style="left:810px;top:1497px;height:787px">
  <header class="site-head">
    <div class="site-logo"><i></i><span>Mended<br>Held<br>Whole</span></div>
    <nav class="nav"><span>Home</span><span>About Us</span><span>Meetings &amp; Events</span><span>Encounter</span><span>Quietwater Chambers / Ministry</span><span class="on">Live Stream &amp; Links</span></nav>
  </header>
  <div class="hero">
    <div class="photo" role="img" aria-label="Broadcast camera filming a worship stage with a lit cross" style="background:linear-gradient(160deg,#1a2030 0%,#4a5a78 45%,#d8b070 65%,#1a1e28 100%)"></div>
    <div class="hero-card" style="height:64px"><span class="dot"></span>Live Stream<br>&amp; Links</div>
  </div>
  <div class="rel center" style="height:254px;padding-top:24px">
    <div class="sec-head">Join Us <b>Live</b></div>
    <p class="lead">We invite you to join our live gatherings online. Whether you're near or far, you can connect with us in real time and be part of our community.</p>
    <div style="margin-top:7px"><span class="btn">Watch Live on StreamVale</span></div>
    <div class="abs frame" role="img" aria-label="Concert-style worship event with stage lights and a large screen" style="left:34px;top:100px;width:150px;height:122px;background:linear-gradient(170deg,#1a2a5a,#4a6ab0 45%,#d87a50 70%,#1a1a2a)"></div>
    <div class="abs" style="left:210px;top:120px;width:110px;text-align:left;color:var(--muted)">
      <div style="font-size:6px;color:var(--green-d);font-weight:500;line-height:1.4">UPCOMING LIVE STREAM<br>SCHEDULE</div>
      <div class="event"><div class="meta" style="margin-top:6px"><span>Sunday, April 6</span><br><span>10:00 AM</span></div></div>
      <div style="color:var(--purple);text-transform:uppercase;margin-top:4px;font-weight:400">StreamVale Live</div>
      <p>Schedule may vary for special events.</p>
      <span class="btn" style="margin-top:6px">Schedule Now</span>
    </div>
  </div>
  <div class="purple center" style="height:87px;padding-top:20px">
    <div class="sec-head">Watch Previous <b>Streams</b></div>
    <p style="width:290px;margin:7px auto 0">If you missed a gathering or would like to revisit a message, you can watch past streams through our online archive.</p>
    <div style="margin-top:6px"><span class="btn">Watch Past Services</span></div>
  </div>
  <div class="rel center" style="height:177px;padding-top:22px">
    <div class="sec-head">Connect On Other <b>Platforms</b></div>
    <p style="color:var(--muted);margin-top:4px">Stay connected with us across our online platforms.</p>
    <div class="card-s" style="left:48px;top:60px;width:78px;height:88px;padding-top:14px;color:var(--muted)"><span style="display:block;width:12px;height:12px;border-radius:50%;background:var(--purple);margin:0 auto 8px"></span><div style="color:var(--green-d);font-weight:400">GATHERBOOK</div>Updates, photos, and community posts</div>
    <div class="card-s" style="left:137px;top:60px;width:78px;height:88px;padding-top:14px;color:var(--muted)"><span style="display:block;width:12px;height:12px;border-radius:50%;background:var(--purple);margin:0 auto 8px"></span><div style="color:var(--green-d);font-weight:400">SNAPLEAF</div>Encouragement, announcements, and highlights</div>
    <div class="card-s" style="left:226px;top:60px;width:78px;height:88px;padding-top:14px;color:var(--muted)"><span style="display:block;width:12px;height:12px;border-radius:3px;background:var(--purple);margin:0 auto 8px"></span><div style="color:var(--green-d);font-weight:400">EMAIL UPDATES</div>Event notices and ministry news</div>
  </div>
  <footer class="site-foot" style="height:117px">
    <div class="foot-brand"><div class="lg"><i></i><span>Mended<br>Held<br>Whole</span></div><div class="social"><i></i><i></i></div></div>
    <div class="foot-col" style="left:135px"><h6>Quick Links</h6>Home<br>About Us<br>Meetings &amp; Events<br>Encounter<br>Quietwater Chambers / Ministry<br>Live Stream &amp; Links</div>
    <div class="foot-col" style="left:232px"><h6>Recent Posts</h6>Nothing is incurable for God<br>Healing amidst the car accident<br>Healing – where and how can it happen?<br>Why is healing important?<br>Now is the time to move</div>
    <div class="copy">Copyright © 2026. All rights reserved.</div>
  </footer>
</section>

</body>
</html>
```